Build a landing page to promote a service (dialler consultation and support).

We are a call centre consultation firm and we need a landing page to promote a service. The service is Korbemix dialler consultation and support.
If you do not know what Korbemix is, please do some quick "Zumbly" research for more information.
The landing page will be promoted with a paid advertisement, so we want something that is simple, and explains exactly what service we offer.
There are two objectives for the landing page:
1) A "call to action" which directs the user to a contact page, including a form plus all of our contact details.
2) A form for them viewers to enter their details to get a "FREE" quote for their project. This form should be placed on the main page.
Notes:
The call to action will require the viewer to enter their name, email, phone number as well as a description of their request. There will also need to be a drop down menu for the type of quote. This menu should have the following options:
1) Korbemix support
2) Korbemix hosting
3) Korbemix customisation
4) Other
We need 2 pages in total:
1) Main landing page
This is the home page. It will need to clearly indicate our services and our key selling features.
Services:
* Korbemix support
* Korbemix hosting
* Korbemix customisation
Key Selling Features:
* Australian based
* PCI complaint
* 10+ years of dialler and call centre experience
* we run a sister company which is a highly reputable 40 seat call centre, so we know first hand about call centre technology.
The main landing page will have an "about us" section with a few paragraphs about how we got started.
-------------------------------------------------------------------------
2) Contact page
All of our contact details will live on this page, as well as a contact form.
Other notes:
We will be self hosting the landing page.
We already have a domain name.
The design must be clean and incorporate our logo, as well as it's colours. (Logo attached)
We want a fully function HTML landing page, not just a "PSD" design.
The page must be mobile optimised.
Target Market(s)
Anyone using Korbemix software.
Coding
Coded - Design and coding required
Number of Pages Required
2 page

```html
<!DOCTYPE html>
<html lang="en">
<head>
<meta charset="utf-8">
<title>Korbemix Dialler Consultation</title>
<link href="https://fonts.googleapis.com/css2?family=Work+Sans:wght@400;500;600;700;800&family=Montserrat:wght@600;700&display=swap" rel="stylesheet">
<style>
:root{
  --orange:#e38a1f;
  --blue:#1d86e2;
  --ink:#161616;
  --text:#444;
  --muted:#777;
  --nav:#1c1c1c;
  --footer:#000;
  --line:#cfcfcf;
  --soft:#f7f7f7;
}
*{margin:0;padding:0;box-sizing:border-box}
html,body{width:1200px;height:3000px;overflow:hidden}
body{position:relative;font-family:"Work Sans",Arial,sans-serif;color:var(--ink);background:#fff}
.abs{position:absolute}

/* nav */
.topbar{position:absolute;left:0;top:0;width:1200px;height:58px;background:var(--nav)}
.brand{position:absolute;left:118px;top:10px;line-height:19px;font-size:19px;color:#fff;font-weight:500}
.brand strong{display:block;color:var(--orange);font-weight:700}
.menu{position:absolute;top:0;right:0;height:58px;display:flex;align-items:center}
.menu a{font-size:12px;color:#ddd;text-decoration:none;margin-right:52px}
.menu a.active{color:var(--orange)}
.menu a:last-child{margin-right:108px}

/* button */
.btn{position:absolute;height:36px;border-radius:18px;background:var(--blue);color:#fff;font-family:Montserrat,Arial,sans-serif;font-size:11px;font-weight:700;display:flex;align-items:center;padding-left:48px;padding-right:18px}
.btn .ring{position:absolute;left:-2px;top:-2px;width:40px;height:40px;border-radius:50%;background:#fff;border:2px solid var(--blue);display:flex;align-items:center;justify-content:center}

/* hero */
.hero{position:absolute;left:0;top:58px;width:1200px;height:588px;background:linear-gradient(90deg,#f3f4f5 0%,#eceef0 45%,#e2e6ea 100%);overflow:hidden}
.hero-photo{position:absolute;left:500px;top:0;width:700px;height:588px;background:linear-gradient(90deg,rgba(236,238,240,0) 0%,#c9d2dc 35%,#9fb0c4 70%,#d9d4ce 100%)}
.hero-kicker{position:absolute;left:112px;top:194px;font-size:30px;letter-spacing:3px;color:var(--ink)}
.hero-title{position:absolute;left:110px;top:228px;font-size:78px;font-weight:700;line-height:80px}
.hero-title .c{color:var(--orange)}
.hero-title .t{color:#0c0c0c;font-weight:800}

/* services */
.svc{position:absolute;top:720px;width:228px;height:158px;background:#fff;box-shadow:0 0 10px rgba(0,0,0,.06);text-align:center}
.svc .label{position:absolute;left:0;right:0;top:102px;font-size:16px;font-weight:500;color:#444}
.svc svg.ic{position:absolute;left:92px;top:38px}
.svc.on{background:var(--orange)}
.svc.on .label{color:#fff}
.corner{position:absolute;border-color:var(--orange);border-style:solid}
.corner.tl{left:-4px;top:-4px;width:40px;height:50px;border-width:1px 0 0 1px}
.corner.br{right:-4px;bottom:-4px;width:40px;height:50px;border-width:0 1px 1px 0}
.dot{position:absolute;width:6px;height:6px;border-radius:50%;background:var(--orange)}

/* features */
.features{position:absolute;left:0;top:1048px;width:1200px;height:534px;background:linear-gradient(90deg,#fafbfb 0%,#f0f2f3 55%,#e6eaee 100%)}
.features-photo{position:absolute;left:720px;top:0;width:480px;height:534px;background:linear-gradient(90deg,rgba(240,242,243,0) 0%,#c7cdd6 30%,#3a4564 60%,#e3e6ea 100%)}
h2.title{position:absolute;font-size:32px;font-weight:500;color:var(--ink)}
.feat-list{position:absolute;left:112px;top:180px;width:570px;list-style:none}
.feat-list li{position:relative;padding-left:56px;font-size:17px;color:#333;line-height:20px;margin-bottom:32px}
.feat-list svg{position:absolute;left:0;top:4px}

/* about */
.about-text{position:absolute;left:112px;top:1822px;width:560px;font-size:12.5px;line-height:22px;color:#444}
.about-text p{margin-bottom:8px}
.orbit{position:absolute;left:680px;top:1730px}

/* quote */
.quote{position:absolute;left:0;top:2212px;width:1200px;height:366px;background:var(--soft)}
.field{position:absolute;border-bottom:1px solid var(--line);font-size:11px;color:#aaa;padding-bottom:6px}

/* footer */
.footer{position:absolute;left:0;top:2578px;width:1200px;height:422px;background:var(--footer);color:#888}
.footer h4{position:absolute;top:68px;font-size:16px;font-weight:500;color:#eee}
.footer .small{font-size:11px;line-height:18px;color:#777}
.links{position:absolute;left:424px;top:124px;list-style:none}
.links li{font-size:11px;color:#888;margin-bottom:16px}
.qa{position:absolute;left:866px}
.qa .h{font-size:13px;color:var(--orange)}
.social{position:absolute;top:252px;display:flex;gap:6px;left:112px}
.social span{width:28px;height:28px;border-radius:50%;background:#fff}
.copy{position:absolute;left:0;width:1200px;top:340px;text-align:center;font-size:10px;color:#555}
</style>
</head>
<body>

<header class="topbar">
  <div class="brand">Korbemix Dialler<strong>Consultation</strong></div>
  <nav class="menu">
    <a class="active">Home</a><a>About</a><a>Service</a><a>Key Feature</a><a>Contact</a>
  </nav>
</header>

<section class="hero">
  <div class="hero-photo" role="img" aria-label="Photo of call centre agents wearing headsets at their desks"></div>
  <div class="hero-kicker">We know first hand about</div>
  <h1 class="hero-title"><span class="c">Call Centre</span><br><span class="t">TECHNOLOGY.</span></h1>
  <div class="btn" style="left:114px;top:404px">
    <span class="ring"><svg width="18" height="18" viewBox="0 0 24 24"><path fill="#1d86e2" d="M6.6 10.8a15 15 0 0 0 6.6 6.6l2.2-2.2c.3-.3.7-.4 1-.2 1.1.4 2.3.6 3.6.6.6 0 1 .4 1 1V20c0 .6-.4 1-1 1A17 17 0 0 1 3 4c0-.6.4-1 1-1h3.5c.6 0 1 .4 1 1 0 1.3.2 2.5.6 3.6.1.3 0 .7-.2 1z"/></svg></span>Contact Us
  </div>
</section>

<section class="services">
  <div class="svc" style="left:114px">
    <span class="corner tl"></span><span class="dot" style="left:-7px;top:-7px"></span>
    <svg class="ic" width="44" height="44" viewBox="0 0 44 44" fill="none" stroke="#555" stroke-width="1.6"><circle cx="24" cy="12" r="5"/><circle cx="24" cy="12" r="2"/><path d="M6 30h6l8 4h10l8-6-3-2-7 4H20M12 30v8H6"/></svg>
    <div class="label">Korbemix Support</div>
  </div>
  <div class="svc" style="left:362px">
    <span class="corner br"></span><span class="dot" style="right:-7px;bottom:-7px"></span>
    <svg class="ic" width="44" height="44" viewBox="0 0 44 44" fill="none" stroke="#555" stroke-width="1.6"><path d="M12 26a7 7 0 0 1 1-14 10 10 0 0 1 19 2 6 6 0 0 1 0 12"/><circle cx="22" cy="20" r="4"/><path d="M22 24v8M14 34h16M16 30l-2 4M28 30l2 4"/></svg>
    <div class="label">Korbemix Hosting</div>
  </div>
  <div class="svc on" style="left:610px">
    <svg class="ic" width="44" height="44" viewBox="0 0 44 44" fill="none" stroke="#fff" stroke-width="1.6"><path d="M10 6l6 2-2 6c2 5 5 8 10 10l6-2 2 6-4 4C18 32 6 20 6 10z"/><circle cx="30" cy="28" r="5"/><circle cx="30" cy="28" r="2"/></svg>
    <div class="label">Korbemix Customisation</div>
  </div>
  <div class="svc" style="left:858px">
    <span class="corner tl"></span><span class="dot" style="left:-7px;top:-7px"></span>
    <span class="corner br"></span><span class="dot" style="right:-7px;bottom:-7px"></span>
    <svg class="ic" width="44" height="44" viewBox="0 0 44 44" fill="none" stroke="#555" stroke-width="1.6"><path d="M10 24v-4a12 12 0 0 1 24 0v4"/><rect x="7" y="22" width="6" height="10" rx="2"/><rect x="31" y="22" width="6" height="10" rx="2"/><path d="M34 32c0 4-4 6-10 6"/><circle cx="22" cy="22" r="6"/></svg>
    <div class="label">Other</div>
  </div>
  <div class="btn" style="left:534px;top:934px">
    <span class="ring"><svg width="18" height="18" viewBox="0 0 24 24"><path fill="#1d86e2" d="M6.6 10.8a15 15 0 0 0 6.6 6.6l2.2-2.2c.3-.3.7-.4 1-.2 1.1.4 2.3.6 3.6.6.6 0 1 .4 1 1V20c0 .6-.4 1-1 1A17 17 0 0 1 3 4c0-.6.4-1 1-1h3.5c.6 0 1 .4 1 1 0 1.3.2 2.5.6 3.6.1.3 0 .7-.2 1z"/></svg></span>View More
  </div>
</section>

<section class="features">
  <div class="features-photo" role="img" aria-label="Photo of a smiling call centre agent with a headset at her desk"></div>
  <h2 class="title" style="left:112px;top:86px">Key Selling Features</h2>
  <ul class="feat-list">
    <li><svg width="16" height="12" viewBox="0 0 16 12" fill="none" stroke="#333" stroke-width="1.4"><path d="M1 2l5 5 3-3 5 5M10 9h4V5"/></svg>Australian Based</li>
    <li><svg width="16" height="12" viewBox="0 0 16 12" fill="none" stroke="#333" stroke-width="1.4"><path d="M1 2l5 5 3-3 5 5M10 9h4V5"/></svg>PCI complaint</li>
    <li><svg width="16" height="12" viewBox="0 0 16 12" fill="none" stroke="#333" stroke-width="1.4"><path d="M1 2l5 5 3-3 5 5M10 9h4V5"/></svg>10+ years of dialler and call centre experience</li>
    <li><svg width="16" height="12" viewBox="0 0 16 12" fill="none" stroke="#333" stroke-width="1.4"><path d="M1 2l5 5 3-3 5 5M10 9h4V5"/></svg>we run a sister company which is a highly reputable 40 seat call centre, so we know first hand about call centre technology.</li>
  </ul>
</section>

<section class="about">
  <h2 class="title" style="left:112px;top:1752px">About Us</h2>
  <div class="about-text">
    <p>It is a long established fact that a reader will be distracted by the readable<br>content of a page when looking at its layout. The point of using Lorem Ipsum is that it has<br>a more-or-less normal distribution of letters,as opposed to using<br>'Content here, content here',</p>
    <p>making it look like readable English. Many desktop publishing packages and web page edi-<br>tors now use Lorem Ipsum as their default model text,and a search for 'lorem ipsum' will<br>uncover many web sites still in their infancy. Various versions have evolved over the years,<br>sometimes by accident.</p>
  </div>
  <div class="btn" style="left:114px;top:2030px">
    <span class="ring"><svg width="18" height="18" viewBox="0 0 24 24"><path fill="#1d86e2" d="M6.6 10.8a15 15 0 0 0 6.6 6.6l2.2-2.2c.3-.3.7-.4 1-.2 1.1.4 2.3.6 3.6.6.6 0 1 .4 1 1V20c0 .6-.4 1-1 1A17 17 0 0 1 3 4c0-.6.4-1 1-1h3.5c.6 0 1 .4 1 1 0 1.3.2 2.5.6 3.6.1.3 0 .7-.2 1z"/></svg></span>Read More
  </div>
  <svg class="orbit" width="420" height="380" viewBox="-20 -10 420 380">
    <circle cx="190" cy="180" r="180" fill="none" stroke="#bbb" stroke-dasharray="3 4"/>
    <circle cx="190" cy="180" r="108" fill="#fff" stroke="var(--blue)" stroke-width="2"/>
    <circle cx="190" cy="180" r="100" fill="#b9c6d4" role="img" aria-label="Photo of a team of call centre agents with headsets"/>
    <g>
      <circle cx="190" cy="32" r="30" fill="#fff" stroke="#bbb"/><circle cx="190" cy="32" r="24" fill="#666"/>
      <circle cx="190" cy="28" r="6" fill="none" stroke="#fff" stroke-width="2"/><path d="M180 42c2-6 18-6 20 0" fill="none" stroke="#fff" stroke-width="2"/>
    </g>
    <g fill="#fff" stroke="var(--blue)" stroke-width="1.5">
      <circle cx="30" cy="136" r="30"/><circle cx="350" cy="136" r="30"/>
      <circle cx="60" cy="318" r="30"/><circle cx="320" cy="318" r="30"/>
    </g>
    <rect x="18" y="126" width="24" height="17" fill="none" stroke="var(--blue)" stroke-width="2"/><path d="M24 148h12" stroke="var(--blue)" stroke-width="2"/>
    <path fill="var(--blue)" d="M346 130a12 12 0 0 0 6 6l2-2 4 1v4c-8 0-16-8-16-16h4l1 4z" transform="translate(-2,-4)"/>
    <path fill="var(--blue)" d="M52 310a12 12 0 0 0 6 6l2-2 4 1v4c-8 0-16-8-16-16h4l1 4zM62 306h8M66 302l4 4-4 4" stroke="var(--blue)" stroke-width="1.5"/>
    <circle cx="320" cy="312" r="5" fill="var(--blue)"/><path d="M310 328c2-8 18-8 20 0z" fill="var(--blue)"/>
    <text x="190" y="344" text-anchor="middle" font-family="Work Sans, Arial, sans-serif" font-size="12" fill="#333">How We Got Started</text>
  </svg>
</section>

<section class="quote">
  <h2 class="title" style="left:112px;top:58px">Get a "FREE" Quote</h2>
  <div class="field" style="left:136px;top:154px;width:296px">Name :</div>
  <div class="field" style="left:460px;top:154px;width:296px">Email :</div>
  <div class="field" style="left:770px;top:154px;width:296px">Phone No :</div>
  <div class="field" style="left:136px;top:216px;width:932px">Description :
    <svg style="position:absolute;right:2px;top:4px" width="8" height="5" viewBox="0 0 8 5"><path d="M0 0h8L4 5z" fill="#999"/></svg>
  </div>
  <div class="btn" style="left:532px;top:270px">
    <span class="ring"><svg width="18" height="18" viewBox="0 0 24 24"><path fill="#1d86e2" d="M6.6 10.8a15 15 0 0 0 6.6 6.6l2.2-2.2c.3-.3.7-.4 1-.2 1.1.4 2.3.6 3.6.6.6 0 1 .4 1 1V20c0 .6-.4 1-1 1A17 17 0 0 1 3 4c0-.6.4-1 1-1h3.5c.6 0 1 .4 1 1 0 1.3.2 2.5.6 3.6.1.3 0 .7-.2 1z"/></svg></span>Submit Now
  </div>
</section>

<footer class="footer">
  <h4 style="left:112px">Korbemix Dialler Consultation</h4>
  <p class="small abs" style="left:112px;top:124px;width:244px">It is a long established fact that a reader will be distracted by the readable content of a page when looking at its layout. The point of using Lorem Ipsum is that it has a more-or-less normal distribution of letters.</p>
  <div class="social"><span></span><span></span><span></span><span></span></div>

  <h4 style="left:424px">Information</h4>
  <ul class="links"><li>Home</li><li>About</li><li>Service</li><li>Key Feature</li><li>Contact</li></ul>

  <h4 style="left:598px">Head Office Location</h4>
  <svg class="abs" style="left:600px;top:126px" width="12" height="16" viewBox="0 0 12 16"><path d="M6 0a6 6 0 0 0-6 6c0 4 6 10 6 10s6-6 6-10a6 6 0 0 0-6-6z" fill="#fff"/><circle cx="6" cy="6" r="2" fill="#000"/></svg>
  <p class="small abs" style="left:632px;top:124px">48 Harlow Lane Brenton,<br>CA 90211 USA</p>
  <svg class="abs" style="left:598px;top:204px" width="16" height="16" viewBox="0 0 16 16" fill="none" stroke="#fff" stroke-width="1.5"><circle cx="8" cy="8" r="7"/><path d="M8 4v4l3 2"/></svg>
  <p class="small abs" style="left:632px;top:202px">Hours<br>Mon - Fri : 10:00 a.m - 6:00 p.m<br>Sat : 10:00 a.m - 3:00 p.m<br>Sun : closed.</p>

  <h4 style="left:864px">You Have any Question?</h4>
  <div class="qa" style="top:126px"><div class="h">Contact us</div><div class="small">000 55555 777</div></div>
  <div class="qa" style="top:184px"><div class="h">Request a Consultation</div><div class="small">Fill Out Form</div></div>
  <div class="qa" style="top:242px"><div class="h">Request a Consultation</div><div class="small">info@korbemixdiallerconsultation.com</div></div>

  <div class="copy">Copyright©2018 Korbemix Dialler Consultation . All Rights Reserved.</div>
</footer>

</body>
</html>
```